Need a fun and informative infographic!

We need an infographic to describe our "client experience" which consists of 4 phases - see info about each of our "phases" which includes our available suite of services. UPDATED THE TEXT IN A NEW FILE CALLED "Client Experience Infographic Info".

We intend to use the infographic in both print and digital in a printed "leave behind", in packets for new clients, and possible on the website.

Keystone Tutorial www.keystonetutorial.example

Target Market(s)

Families of children aged Kindergarten through 12th Grade; affluent communities who have expendable income to spend on private tutoring and test prep.

Industry/Entity Type

Education

Font styles to use
Sans Serif

Requirements
Must have
• My project must use our brand colors.
• Light Blue CMYK: 60 27 0 0 RGB: 115 165 215
• Dark Blue CMYK: 93 85 36 27 RGB: 43 57 94
• Orange CMYK: 0 46 77 10 RGB: 230 125 53

```html
<!DOCTYPE html>
<html lang="en">
<head>
<meta charset="utf-8">
<title>The Client Experience – Keystone Tutorial</title>
<link rel="stylesheet" href="https://fonts.googleapis.com/css2?family=Roboto+Condensed:wght@700&family=Open+Sans:wght@400;600;700&display=swap">
<style>
  :root {
    --orange: #e67d35;
    --blue: #7d9fcd;
    --dark-blue: #2b395e;
    --title-blue: #5f86c4;
    --text: #1f2535;
    --white: #ffffff;
    --logo-grey: #6f7680;
  }
  * { box-sizing: border-box; margin: 0; padding: 0; }
  html, body { width: 761px; height: 1200px; overflow: hidden; background: var(--white); }
  body { font-family: "Open Sans", Arial, sans-serif; color: var(--text); position: relative; }

  .header {
    position: absolute; left: 0; top: 0; width: 761px; height: 182px;
    background: var(--orange); text-align: center;
  }
  .header__title {
    font-family: "Roboto Condensed", Arial, sans-serif; font-weight: 700;
    font-size: 42px; line-height: 40px; letter-spacing: 1px;
    color: var(--title-blue); -webkit-text-stroke: 1.5px var(--dark-blue);
    padding-top: 32px;
  }
  .header__brand {
    margin-top: 14px; font-family: "Open Sans", Arial, sans-serif;
    font-weight: 400; font-size: 25px; color: var(--logo-grey);
  }

  .phase { position: absolute; left: 0; width: 761px; }
  .phase--orange { background: var(--orange); }
  .phase--blue { background: var(--blue); }
  .phase--one { top: 202px; height: 234px; }
  .phase--two { top: 460px; height: 232px; }
  .phase--three { top: 713px; height: 234px; }
  .phase--four { top: 968px; height: 232px; }

  .phase__number {
    position: absolute; left: 23px; top: 52px; width: 160px; height: 160px;
    border: 10px solid var(--white); border-radius: 50%;
    display: flex; align-items: center; justify-content: center;
    font-family: "Open Sans", Arial, sans-serif; font-weight: 600;
    font-size: 96px; color: var(--white);
  }
  .phase__art { position: absolute; border-radius: 6px; }
  .phase--one .phase__art { left: 152px; top: 70px; width: 225px; height: 132px;
    background: linear-gradient(135deg, #f0b08a, #c9524f 60%, #4a6a55); }
  .phase--two .phase__art { left: 226px; top: 50px; width: 124px; height: 150px;
    background: linear-gradient(180deg, #ffffff, #e8ecf4); border: 3px solid var(--dark-blue); }
  .phase--three .phase__art { left: 170px; top: 52px; width: 196px; height: 155px;
    background: linear-gradient(135deg, #f3f3f3, #9fb4d4 55%, #7a4a2e); }
  .phase--four .phase__art { left: 180px; top: 42px; width: 170px; height: 170px;
    background: linear-gradient(160deg, #dfe3ea, #a4adba 50%, #6b3f25); }

  .phase__heading { position: absolute; left: 380px; width: 380px; text-align: center; top: 14px; }
  .phase--four .phase__heading { left: 350px; width: 400px; }
  .phase__label { font-weight: 600; font-size: 14px; color: #2a2a2a; }
  .phase__name { font-weight: 600; font-size: 19px; color: var(--text); margin-top: 2px; }

  .phase__points { position: absolute; list-style: none; font-size: 9.5px; line-height: 13.5px; font-weight: 600; }
  .phase__points li { position: relative; padding-left: 13px; }
  .phase__points li::before {
    content: ""; position: absolute; left: 0; top: 5px; width: 4px; height: 4px;
    border-radius: 50%; background: var(--dark-blue);
  }
  .phase__points .sub { list-style: none; padding-left: 6px; }
  .phase__points .sub li { padding-left: 8px; }
  .phase__points .sub li::before { content: "-"; background: none; width: auto; height: auto; top: 0; }
</style>
</head>
<body>

<header class="header">
  <h1 class="header__title">THE CLIENT<br>EXPERIENCE</h1>
  <p class="header__brand">Keystone Tutorial</p>
</header>

<section class="phase phase--orange phase--one">
  <div class="phase__number">1</div>
  <div class="phase__art" role="img" aria-label="Illustration of parents and student asking questions during a consultation"></div>
  <div class="phase__heading">
    <p class="phase__label">Phrase 1</p>
    <h2 class="phase__name">The Consultation</h2>
  </div>
  <ul class="phase__points" style="left:393px; top:100px; width:125px;">
    <li>The process begins with a complimentary and thorough consultation.</li>
  </ul>
  <ul class="phase__points" style="left:562px; top:100px; width:180px;">
    <li>One of our local Educational Directors meets in-person (or via VidLink if necessary) with the parents and student to become acquainted and to better understand the family's needs.</li>
  </ul>
</section>

<section class="phase phase--blue phase--two">
  <div class="phase__number">2</div>
  <div class="phase__art" role="img" aria-label="Illustration of a tutor profile card with a checklist"></div>
  <div class="phase__heading">
    <p class="phase__label">Phrase 2</p>
    <h2 class="phase__name">Match and Customize</h2>
  </div>
  <ul class="phase__points" style="left:386px; top:86px; width:155px;">
    <li>Students are matched with a tutor or a team of tutors based on a careful understanding of each student's unique learning style, academic goals, personality, and schedule.</li>
  </ul>
  <ul class="phase__points" style="left:568px; top:86px; width:193px;">
    <li>The tutor(s) develop a personalized curriculum that aligns with the student's existing strengths and areas for improvement, while addressing all factors impacting performance such as test anxiety and self-confidence.</li>
  </ul>
</section>

<section class="phase phase--orange phase--three">
  <div class="phase__number">3</div>
  <div class="phase__art" role="img" aria-label="Illustration of a tablet showing grades beside a tutor and a screen"></div>
  <div class="phase__heading">
    <p class="phase__label">Phrase 3</p>
    <h2 class="phase__name">Communication</h2>
  </div>
  <ul class="phase__points" style="left:382px; top:80px; width:155px;">
    <li>Tutoring sessions occur in the home, our offices, remotely or a location of the family's choosing; scheduling is based on the availability of the student.</li>
  </ul>
  <ul class="phase__points" style="left:573px; top:80px; width:178px;">
    <li>Our custom-built "Dashboard" allows parents and our Directors to receive a thorough "Lesson Summary" after each session giving them a detailed review of the tutoring session and the student's homework for the coming week.</li>
  </ul>
</section>

<section class="phase phase--blue phase--four">
  <div class="phase__number">4</div>
  <div class="phase__art" role="img" aria-label="Illustration of an educational director with gears"></div>
  <div class="phase__heading">
    <p class="phase__label" style="font-size:17px;">Ongoing:</p>
    <h2 class="phase__name">Our Suite of Services</h2>
  </div>
  <ul class="phase__points" style="left:360px; top:76px; width:125px;">
    <li>Our Educational Directors are compassionate and responsive, ready to provide guidance and seamless coordination of whatever services the student requires.</li>
  </ul>
  <ul class="phase__points" style="left:490px; top:76px; width:140px;">
    <li>No matter where along the path our relationship begins, we continue to support our students and families in a myriad of ways including:
      <ul class="sub">
        <li>Standardized Test Prep</li>
        <li>Subject Tutoring</li>
        <li>College Admissions</li>
      </ul>
    </li>
  </ul>
  <ul class="phase__points" style="left:643px; top:76px; width:118px;">
    <li>When appropriate, we introduce behaviors for students to improve their executive functioning, organizational and time management</li>
  </ul>
</section>

</body>
</html>
```